Voyage "FUN & RENCONTRES" réservé aux +21
Besoins
Fort de nos compétences, notre agence a été la première à développer les concepts "spring break" en Belgique francophone en réunissant des centaines d'étudiants en Espagne pour faire la fête !
Suite à un souci de santé, notre graphiste habituel ne peut s'occuper de nos réalisations.
Nous recherchons une personne sur le long terme (= si travail sérieux, échanges de coordonnées et autres "contrats").
Il nous faudra également une couverture facebook (cover) et une affiche format A4 recto seul.
Le nom du concept est COASTAL GLOW.
Vous être libre de me créer un beau et nouveau logo bien entendu.
Celui-ci pourra éventuellement être mis sur des futurs t-shirts pour notre staff d'animateurs pendant le voyage ou offert au public !
Voici le travail à effectuer :
- Objectif NOUVEAU CONCEPT 2018 en Bulgarie -
Il nous faut un visuel (flyer efficace et dynamique pour attirer une population entre 21 et 35 ans.
Idée du flyers : format carte postale A6 paysage, vintage, avec un beau visuel au recto qui donne envie et éveille la curiosité (avec titre du voyage "COASTAL GLOW - Bulgarie 2018") et la mention "New Concept" avec notre logo MIRALDO TRAVEL.
Au verso, sur la moitier gauche de la carte postale : petit mot doux d'une femme, du style "Hey ! Le soleil est bien là, les cocktails sont savoureux et l'ambiance incroyable ! On t'attends avec les filles ! Je t'embrasse. Lena" avec un faux baiser (= smack).
Sur la moitier droite, les informations utiles au séjours à savoir :
- du samedi 1 au samedi 8 septembre 2018 (format au choix pour la date)
- Roches Claires, Bulgarie
- Voyage "tout compris" : vol aller-retour, hôtel 4**** formule ALL INCLUSIVE, entrées en boites, cocktails offerts, beach party, ... & bien plus !
- prix : € 599,00 par personne en chambre double
- plus d'infos sur www.coastal-glow-demo.com ou au 0471 820 946
Ci-joint le logo de notre agence + quelques visuels de notre dernier voyage en Hongrie (histoire de vous donner un peu l'effet à ressentir ATTENTION je veux autre chose ici pas du copier coller svp merci)
Bonne chance à tous !
La cible
Public entre 21 et 35 ans - aiment la fête, le soleil et les nouvelles rencontres
Couleurs, favoris et autres exigences:
Couleurs chaudes, festives

```html
<!DOCTYPE html>
<html lang="fr">
<head>
<meta charset="utf-8">
<title>Coastal Glow – Carte postale verso</title>
<link rel="stylesheet" href="https://fonts.googleapis.com/css2?family=Oswald:wght@300;400&family=Parisienne&display=swap">
<style>
  :root {
    --paper: #ffffff;
    --ink: #1f1f1f;
    --muted: #6d6d6d;
    --red: #e2312b;
    --orange: #f08a1c;
    --orange-deep: #ee6a12;
    --yellow: #f7b733;
    --lip: #d8262b;
    --edge: #d9d9d9;
  }
  * { margin: 0; padding: 0; box-sizing: border-box; }
  html, body { width: 1200px; height: 854px; overflow: hidden; background: var(--paper); }
  .postcard {
    position: relative; width: 1200px; height: 854px;
    background: var(--paper); border: 2px solid var(--edge); overflow: hidden;
    font-family: "Oswald", sans-serif; color: var(--ink);
  }
  .confetti-area {
    position: absolute; left: 0; top: 0; width: 560px; height: 190px;
    background: radial-gradient(ellipse at 40% 20%, rgba(247,183,51,.28), rgba(240,138,28,.12) 45%, rgba(255,255,255,0) 75%);
  }
  .note {
    position: absolute; left: 70px; top: 130px;
    font-family: "Parisienne", cursive; font-size: 40px; line-height: 68px; color: var(--ink);
  }
  .note p { white-space: nowrap; }
  .note .sign-off { margin-top: 18px; }
  .signature {
    position: absolute; left: 372px; top: 600px;
    font-family: "Parisienne", cursive; font-size: 32px; color: var(--ink);
  }
  .kiss {
    position: absolute; left: 170px; top: 625px; width: 140px; height: 90px;
    border-radius: 50% 50% 48% 48% / 55% 55% 45% 45%;
    background: radial-gradient(ellipse at 50% 45%, #e8484a, var(--lip) 60%, rgba(216,38,43,.6));
  }
  .dates {
    position: absolute; left: 452px; top: 52px; width: 340px; height: 110px;
    background: linear-gradient(90deg, var(--yellow), var(--orange) 55%, var(--orange-deep));
    transform: rotate(-8deg); transform-origin: left bottom;
    color: #fff; display: flex; align-items: center; justify-content: space-between;
    padding: 0 22px; text-transform: uppercase;
  }
  .dates .day { font-size: 20px; line-height: 1; font-weight: 300; letter-spacing: 1px; }
  .dates .day strong { display: block; font-size: 38px; font-weight: 400; line-height: 1.05; }
  .dates .palm { width: 26px; height: 26px; border-radius: 50%; background: rgba(255,255,255,.85); }
  .title {
    position: absolute; left: 1125px; top: 30px; width: 540px;
    transform: rotate(90deg); transform-origin: left top;
    font-size: 50px; font-weight: 300; letter-spacing: 4px; color: var(--red);
    white-space: nowrap; line-height: 1;
  }
  .destination {
    position: absolute; left: 505px; top: 250px;
    font-family: "Parisienne", cursive; font-size: 50px; color: var(--orange);
    transform: rotate(-5deg); white-space: nowrap;
  }
  .inclusions {
    position: absolute; right: 258px; top: 345px; text-align: right;
    transform: rotate(-4deg); transform-origin: right top;
    list-style: none; font-size: 37px; line-height: 42px; text-transform: uppercase;
  }
  .inclusions sup { color: var(--orange); font-size: 20px; letter-spacing: 1px; }
  .inclusions .more {
    font-family: "Parisienne", cursive; text-transform: none; color: var(--orange); font-size: 32px;
  }
  .price {
    position: absolute; left: 520px; top: 660px; width: 265px; height: 90px;
    background: linear-gradient(90deg, var(--orange), var(--orange-deep));
    transform: rotate(-7deg); color: #fff; text-align: center; padding-top: 10px;
  }
  .price .amount { font-size: 34px; font-weight: 300; letter-spacing: 1px; line-height: 1.1; }
  .price .terms { font-size: 13px; font-weight: 300; letter-spacing: .5px; text-transform: uppercase; }
  .contact {
    position: absolute; left: 28px; right: 60px; bottom: 16px;
    display: flex; justify-content: space-between;
    font-size: 21px; font-weight: 300; letter-spacing: 3px; color: var(--muted); text-transform: uppercase;
  }
  .contact .site, .contact .phone { color: var(--ink); font-weight: 400; text-transform: none; }
</style>
</head>
<body>
  <main class="postcard">
    <div class="confetti-area" role="img" aria-label="Confettis orange et jaune en pluie"></div>

    <section class="note">
      <p>Hey !</p>
      <p>Le soleil est bien là,</p>
      <p>les cocktails sont savoureux</p>
      <p>et l'ambiance incroyable !</p>
      <p>On t'attends avec les filles !</p>
      <p class="sign-off">Je t'embrasse.</p>
    </section>
    <div class="signature">Lena</div>
    <div class="kiss" role="img" aria-label="Trace de baiser au rouge à lèvres"></div>

    <div class="dates">
      <div class="day">Du samedi<strong>1-09-18</strong></div>
      <div class="palm" role="img" aria-label="Petit palmier"></div>
      <div class="day">Au samedi<strong>8-09-18</strong></div>
    </div>

    <h1 class="title">Voyage «Tout compris»</h1>

    <h2 class="destination">Roches Claires, Bulgarie</h2>

    <ul class="inclusions">
      <li>Vol aller-retour,</li>
      <li>Hôtel 4<sup>****</sup></li>
      <li>Formule all inclusive,</li>
      <li>Entrées en boîte,</li>
      <li>Cocktails offerts,</li>
      <li>Beach party</li>
      <li class="more">... et bien plus !</li>
    </ul>

    <div class="price">
      <p class="amount">PRIX : 599,00 €</p>
      <p class="terms">Par personne en chambre double</p>
    </div>

    <footer class="contact">
      <span>Plus d'infos sur <span class="site">www.coastal-glow-demo.com</span></span>
      <span>ou au <span class="phone">0471 820 946</span></span>
    </footer>
  </main>
</body>
</html>
```